House-share and Room Rental Website (With Focus on the Bedroom Landing Page)

Looking for website design for our House-share (executive accommodation) and room rental business.

Our company name is: Lodvenra could also be written as LodVenra or lodvenra. Either is fine .. just looking for a nice clean catchy logo to go with the design.

EXAMPLES
These are examples of other websites in this field that are doing well. this is a kind of baseline.
https://kelbrin.com.au/
https://www.tuvaplex.com/
https://www.nestorvi.com/
https://www.quillsa.net/
https://www.pendlebarrow.com.au/

Our business model is to rent rooms to people looking for high-quality accommodation. We fill the gap between those looking to rent rooms and those with rooms to rent. However, our model is slightly different from those already on the market as we looking to fill a massive gap in the market delivering upmarket rooms for rent.(Executive Accommodation) also in the back end will be coupled with a self management process in the back end.

We offer executive style accommodation that stands out above the rest. With special extras like fire safety.. and management processes that create happier homes. We are looking for a web design package that can help us grow and scale our business. We need a design that is captivating

Our MAIN focus is having a room landing page that stands out from the rest... The core of our business will rely on the promotion of the rooms in a share house... so the whole design relies on the BEDROOM landing page to drive results.

Target Market(s)

We have 2 markets we are aiming at ... the first market is people offering rooms to rent who want the highest rental return. The second market is people looking to rent safe, high-quality rooms, in houses that are well managed and looked after.

Industry/Entity Type

Share Economy

Logo Text

LodVenra

Number of Pages Required

5+ page

Font styles to use
Sans Serif

Colors
3276b5

Requirements
Must have
• A messaging system whereby we can create direct communication between those offering rooms and those looking for rooms.
• A call to action that says " Schedule an Inspection"
• Landing page for promoting rooms
• A home page for showing stock.
• Profile page for those selling rooms
• Profile page for those looking for rooms.
• A scheduling calendar for booking inspections
Nice to have
• Pages where new residents can lock in a room.. pay bond and rents.. and sign contracts
• Notifications
• SMS capabilities in the backend.
Should not have
• No script or handwriting fonts.

```html
<!DOCTYPE html>
<html lang="en">
<head>
<meta charset="utf-8">
<title>Lodvenra – Room</title>
<link href="https://fonts.googleapis.com/css2?family=Open+Sans:wght@400;600&family=Raleway:wght@500;600;700&display=swap" rel="stylesheet">
<style>
:root{
  --brand:#3276b5;
  --accent:#f26b1d;
  --page:#f4f4f4;
  --card:#ffffff;
  --line:#e6e6e6;
  --text:#555b61;
  --muted:#9a9fa4;
  --white:#ffffff;
  --hero-dark:#2b2926;
  --hero-mid:#5a554d;
  --hero-warm:#8c8070;
  --map-green:#c8d7b4;
  --map-water:#a7c4ea;
  --map-land:#e4dfd4;
}
*{box-sizing:border-box;margin:0;padding:0}
html,body{width:781px;height:1200px;overflow:hidden}
body{background:var(--page);font-family:"Open Sans",sans-serif;color:var(--text);position:relative}
.hero{position:absolute;left:0;top:0;width:781px;height:404px;background:var(--hero-dark)}
.hero-photo{position:absolute;inset:0;
  background:
    radial-gradient(ellipse 55% 40% at 50% 62%,rgba(140,128,112,.55) 0%,rgba(140,128,112,0) 100%),
    linear-gradient(180deg,var(--hero-dark) 0%,var(--hero-mid) 38%,#4a463f 62%,#3a3733 100%)}
.brand{position:absolute;left:74px;top:17px;font-family:"Raleway",sans-serif;font-weight:500;font-size:18px;color:var(--white);letter-spacing:.3px}
.top-nav{position:absolute;right:73px;top:23px;display:flex;align-items:center;gap:18px;color:var(--white)}
.top-nav .login{font-size:7.5px;font-weight:600;display:flex;align-items:center;gap:6px}
.top-nav .phone{font-family:"Raleway",sans-serif;font-size:11px;font-weight:600;display:flex;align-items:center;gap:6px}
.room-panel{position:absolute;left:244px;top:213px;width:292px;height:110px;background:rgba(40,38,36,.45)}
.room-title{position:absolute;left:256px;top:226px;font-family:"Raleway",sans-serif;font-weight:700;font-size:25px;color:var(--white)}
.room-sub{position:absolute;left:256px;top:261px;display:flex;align-items:center;gap:6px;font-size:11.5px;color:var(--white)}
.map-btn{background:var(--accent);color:var(--white);font-size:7px;padding:4px 7px;font-weight:600}
.room-facts{position:absolute;left:256px;top:286px;display:flex;gap:26px;color:var(--white);font-size:8.5px;font-weight:600}
.room-facts span{display:flex;align-items:center;gap:8px}
.scroll-cue{position:absolute;left:371px;top:385px;width:39px;height:39px;border-radius:50%;background:var(--page);display:flex;justify-content:center;padding-top:11px}
.search-bar{position:absolute;left:96px;top:437px;display:flex;gap:8px}
.field{width:111px;height:25px;background:var(--card);border:1px solid var(--line);font-size:7.5px;color:var(--text);display:flex;align-items:center;justify-content:center;gap:8px}
.search-btn{width:112px;height:25px;background:var(--brand);color:var(--white);font-size:8px;font-weight:600;display:flex;align-items:center;justify-content:center;margin-left:1px}
.card{position:absolute;background:var(--card);border:1px solid #ececec}
.card h2{font-family:"Raleway",sans-serif;font-weight:600;font-size:11.5px;color:var(--brand)}
.description{left:72px;top:495px;width:364px;height:214px;padding:10px 11px}
.description p{font-size:7px;line-height:14.4px;margin-top:8px;color:#5f646a}
.description p+p{margin-top:9px}
.features{left:457px;top:495px;width:252px;height:214px;padding:10px 11px}
.feature-grid{display:grid;grid-template-columns:118px 118px;row-gap:14px;margin-top:11px}
.feature{display:flex;align-items:center;gap:7px;font-size:8.4px;color:var(--text);height:20px}
.feature svg{flex:none}
.map-card{left:72px;top:729px;width:637px;height:274px}
.map-card h2{text-align:center;margin-top:23px}
.map{position:absolute;left:0;top:63px;width:636px;height:210px;
  background:linear-gradient(90deg,var(--map-green) 0%,var(--map-land) 14%,var(--map-water) 24%,var(--map-water) 30%,var(--map-land) 42%,var(--map-land) 100%)}
.footer{position:absolute;left:0;top:1048px;width:781px;height:152px;background:var(--card)}
.footer-brand{position:absolute;left:72px;top:20px;font-family:"Raleway",sans-serif;font-weight:500;font-size:15px;color:var(--brand)}
.footer-links{position:absolute;right:74px;top:24px;display:flex;gap:37px;font-size:8px;color:var(--text)}
.footer-rule{position:absolute;left:72px;top:62px;width:637px;height:1px;background:var(--line)}
.social{position:absolute;left:343px;top:81px;display:flex;gap:18px}
.social span{width:10px;height:10px;border-radius:50%;background:#b9bdc1}
.copyright{position:absolute;left:0;width:781px;top:107px;text-align:center;font-size:6.5px;color:#b7babd}
</style>
</head>
<body>
<header class="hero">
  <div class="hero-photo" role="img" aria-label="Photo of a modern bedroom with a large bed, wood panelling and a window"></div>
  <div class="brand">lodvenra</div>
  <nav class="top-nav">
    <span class="login"><svg width="11" height="11" viewBox="0 0 12 12" fill="none" stroke="#fff" stroke-width="1"><circle cx="6" cy="4" r="2.6"/><path d="M1.5 11.5c0-2.6 2-4.2 4.5-4.2s4.5 1.6 4.5 4.2"/></svg>LOG IN/SIGN UP</span>
    <span class="phone"><svg width="11" height="11" viewBox="0 0 12 12" fill="#fff"><path d="M2.5 1l2 2.3-1 1.4c.7 1.5 1.8 2.6 3.3 3.3l1.4-1L10.5 9 9.2 10.8C5 10.5 1.5 7 1.2 2.8z"/></svg>010-4827391</span>
  </nav>
  <div class="room-panel"></div>
  <h1 class="room-title">Contrary To Popular</h1>
  <div class="room-sub">Lorem Ipsum is not simply random text <span class="map-btn">View on Map</span></div>
  <div class="room-facts">
    <span><svg width="20" height="18" viewBox="0 0 20 18" fill="none" stroke="#fff" stroke-width="1"><path d="M4 2h12v7H4zM2 9h16v5H2zM3 14v3M17 14v3M6 5h8"/></svg>2 Bed</span>
    <span><svg width="26" height="20" viewBox="0 0 26 20" fill="none" stroke="#fff" stroke-width="1"><path d="M8 10c2-5 8-7 12-5M20 5l4-3M6 12l-2 6M9 13l-1 6M12 13l1 5M5 15l6-1"/></svg>2 Bathroom</span>
    <span><svg width="20" height="20" viewBox="0 0 20 20" fill="none" stroke="#fff" stroke-width="1"><circle cx="10" cy="7" r="5"/><path d="M2 19c0-4 4-6 8-6s8 2 8 6"/></svg>4 Persons</span>
  </div>
  <div class="scroll-cue"><svg width="10" height="6" viewBox="0 0 10 6" fill="none" stroke="#777" stroke-width="1.2"><path d="M1 1l4 4 4-4"/></svg></div>
</header>

<form class="search-bar">
  <div class="field">ALL PROPERTIES <svg width="7" height="4" viewBox="0 0 7 4" fill="none" stroke="#666"><path d="M.5.5l3 3 3-3"/></svg></div>
  <div class="field">Arrival Date <svg width="7" height="4" viewBox="0 0 7 4" fill="none" stroke="#666"><path d="M.5.5l3 3 3-3"/></svg></div>
  <div class="field">Departure Date <svg width="7" height="4" viewBox="0 0 7 4" fill="none" stroke="#666"><path d="M.5.5l3 3 3-3"/></svg></div>
  <div class="field">All Locations <svg width="7" height="4" viewBox="0 0 7 4" fill="none" stroke="#666"><path d="M.5.5l3 3 3-3"/></svg></div>
  <div class="search-btn">SEARCH</div>
</form>

<section class="card description">
  <h2>Description</h2>
  <p>Contrary to popular belief, Lorem Ipsum is not simply random text. It has roots in a pieh classical Latin literature from 45 BC, making it over 2000 years old. Edwin Marlowe,professor at Ashgrove College in Virginia, looked up one of the more obscure Latin words, consectet a Lorem Ipsum passage, and going through the cites of the word in classical literature, discovered the undoubtablource. Lorem Ipsum comes from sections 1.10.32 and 1.10.33 of "de Finibus Bonorum et Malorum" (The Extremes of Good and Evil) by Tullian, written in 45 BC. This book is a treatise on the theory of ethics,</p>
  <p>Contrary to popular belief, Lorem Ipsum is not simply random text. It has roots in a pieh classical Latin literature from 45 BC, making it over 2000 years old. Edwin Marlowe,professor at Ashgrove College in Virginia, looked up one of the more obscure Latin words, consectet a Lorem Ipsum passage, and going through the cites of the word in classical literature, discovered.</p>
</section>

<section class="card features">
  <h2>Features</h2>
  <div class="feature-grid">
    <div class="feature"><svg width="19" height="17" viewBox="0 0 18 16" fill="none" stroke="#8a8f94" stroke-width=".9"><path d="M1 13l8-4 8 4-8 2zM4 10l3-7 7 3"/></svg>Size of room</div>
    <div class="feature"><svg width="19" height="17" viewBox="0 0 18 16" fill="none" stroke="#8a8f94" stroke-width=".9"><rect x="3" y="5" width="12" height="6" rx="3" transform="rotate(-40 9 8)"/></svg>internet speed</div>
    <div class="feature"><svg width="19" height="19" viewBox="0 0 18 18" fill="none" stroke="#8a8f94" stroke-width=".9"><circle cx="9" cy="9" r="8"/><path d="M4 13h10M5 13V8h8v5M7 8v5M11 8v5"/></svg>Furnished terrace</div>
    <div class="feature"><svg width="19" height="17" viewBox="0 0 18 16" fill="none" stroke="#8a8f94" stroke-width=".9"><path d="M3 8c2-5 8-6 12-4M5 10l-1 5M8 11v4M11 10l1 5"/></svg>Ensuite shower</div>
    <div class="feature"><svg width="19" height="19" viewBox="0 0 18 18" fill="none" stroke="#8a8f94" stroke-width=".9"><path d="M2 17V8h6v9M8 17V3h6v14M2 17h14"/></svg>Kitchen</div>
    <div class="feature"><svg width="19" height="17" viewBox="0 0 18 16" fill="none" stroke="#8a8f94" stroke-width=".9"><rect x="1" y="1" width="16" height="11"/><path d="M7 4l4 2.5L7 9zM6 15h6"/></svg>best Tv Units</div>
    <div class="feature"><svg width="19" height="19" viewBox="0 0 18 18" fill="none" stroke="#8a8f94" stroke-width=".9"><path d="M2 16l14-14M3 6h5v3H3zM10 11h5v4h-5"/></svg>Living Area</div>
    <div class="feature"><svg width="19" height="19" viewBox="0 0 18 18" fill="none" stroke="#8a8f94" stroke-width=".9"><rect x="2" y="1" width="14" height="16"/><path d="M2 6h14M9 6v11M2 11h7"/></svg>Wardrobe</div>
    <div class="feature"><svg width="21" height="19" viewBox="0 0 20 18" fill="none" stroke="#8a8f94" stroke-width=".9"><rect x="1" y="4" width="13" height="9"/><path d="M5 16h5M7.5 13v3M15 2h4v15h-4z"/></svg>Workstation</div>
    <div class="feature"><svg width="19" height="17" viewBox="0 0 18 16" fill="none" stroke="#8a8f94" stroke-width=".9"><path d="M3 8c2-5 8-6 12-4M5 10l-1 5M8 11v4M11 10l1 5"/></svg>Ensuite shower</div>
  </div>
</section>

<section class="card map-card">
  <h2>Map Location</h2>
  <div class="map" role="img" aria-label="Street map of the area around the property, with a river on the left"></div>
</section>

<footer class="footer">
  <div class="footer-brand">lodvenra</div>
  <nav class="footer-links"><span>Privacy</span><span>Terms</span><span>Careers</span><span>FAQs</span><span>Press Pack</span></nav>
  <div class="footer-rule"></div>
  <div class="social" aria-label="Social links"><span></span><span></span><span></span><span></span></div>
  <div class="copyright">Copyrights 2018 © All Rights Reserved</div>
</footer>
</body>
</html>
```